Building company buisness cards

We are looking for a sharp modern new look for our business cards.
We are a New Zealand based company that specialises in house and land packages.
We have attached a photo of the current logo and would like to see if it can be improved somehow if needed.
We are open to any colours but we have chosen green at this stage.
Feel free to change the font and make the logo smarter looking.
Play with the colours and see what looks best.

We want a card that looks so good know one will want to throw it away!

Target Market(s)

Home buyers

Industry/Entity Type

Building

Contact Information for Business Card

Dorian Keswick
0217392604
dkeswick@tidewellhomecraft.co.nz
tidewellhomecraft.co.nz

Font styles to use
Serif
Sans Serif

Colors

Designer to choose colors to be used in the design.

Requirements
Must have
• Logo and company name on one side, details on the other side
Nice to have
• Color codes for the original green are HEX #4a8028, RGB(74,128,40), CMYK(42,0,69,50)
• Round corners, Raised and/or spot UV

```html
<!DOCTYPE html>
<html lang="en">
<head>
<meta charset="utf-8">
<title>Tidewell Homecraft – Business Cards</title>
<link href="https://fonts.googleapis.com/css2?family=Montserrat:wght@500;700;800&display=swap" rel="stylesheet">
<style>
  :root {
    --stage: #353535;
    --brand-green: #4a8328;
    --brand-green-deep: #3f7322;
    --paper: #ffffff;
    --ink-light: #ffffff;
    --ghost-on-green: rgba(30, 70, 15, 0.35);
    --ghost-on-white: rgba(74, 128, 40, 0.16);
  }
  * { margin: 0; padding: 0; box-sizing: border-box; }
  html, body {
    width: 1092px;
    height: 1200px;
    overflow: hidden;
    background: var(--stage);
    font-family: "Montserrat", Arial, sans-serif;
  }
  .card {
    position: absolute;
    left: 224px;
    width: 644px;
    height: 364px;
    border-radius: 18px;
    overflow: hidden;
  }
  .card--details { top: 204px; background: var(--brand-green); color: var(--ink-light); }
  .card--brand { top: 635px; background: var(--paper); color: var(--brand-green); }

  .brand-decoration {
    position: absolute;
    right: 0;
    top: 60px;
    width: 230px;
    height: 304px;
  }
  .card--details .brand-decoration {
    background: linear-gradient(160deg, var(--ghost-on-green), rgba(30,70,15,0.08));
  }
  .card--brand .brand-decoration {
    top: 70px;
    right: 0;
    width: 240px;
    height: 294px;
    background: linear-gradient(160deg, var(--ghost-on-white), rgba(74,128,40,0.03));
  }

  .details-wordmark {
    position: absolute;
    left: 152px;
    top: 50px;
    display: flex;
    align-items: center;
    gap: 12px;
    font-weight: 800;
    font-size: 27px;
    line-height: 1;
    letter-spacing: -0.3px;
  }
  .details-wordmark .mark-square {
    width: 30px;
    height: 30px;
    background: var(--ink-light);
  }
  .person-name {
    position: absolute;
    left: 114px;
    top: 152px;
    font-weight: 700;
    font-size: 31px;
    letter-spacing: 2px;
  }
  .contact-list {
    position: absolute;
    left: 114px;
    top: 214px;
    list-style: none;
    font-weight: 500;
    font-size: 17px;
    letter-spacing: 1.6px;
  }
  .contact-list li { height: 39px; }

  .brand-lockup {
    position: absolute;
    left: 0;
    right: 0;
    top: 80px;
    text-align: center;
    font-weight: 800;
  }
  .brand-lockup .mark-square {
    display: block;
    width: 52px;
    height: 52px;
    margin: 0 auto 26px;
    background: var(--brand-green);
  }
  .brand-name {
    line-height: 1;
    letter-spacing: -0.5px;
  }
  .brand-name .line-1 { display: block; font-size: 42px; }
  .brand-name .line-2 { display: block; font-size: 55px; margin-top: 2px; }
  .brand-rule {
    width: 344px;
    height: 2px;
    margin: 12px auto 14px;
    background: var(--brand-green);
  }
  .brand-url {
    font-weight: 700;
    font-size: 19px;
    letter-spacing: 1.6px;
  }
</style>
</head>
<body>
  <section class="card card--details" aria-label="Business card, details side">
    <div class="brand-decoration" role="img" aria-label="Faint enlarged brand symbol decoration"></div>
    <div class="details-wordmark"><span class="mark-square"></span><span>tidewell home plans.</span></div>
    <h1 class="person-name">Dorian Keswick</h1>
    <ul class="contact-list">
      <li>0217392604</li>
      <li>dkeswick@tidewellhomecraft.co.nz</li>
      <li>tidewellhomecraft.co.nz</li>
    </ul>
  </section>

  <section class="card card--brand" aria-label="Business card, brand side">
    <div class="brand-decoration" role="img" aria-label="Faint enlarged brand symbol decoration"></div>
    <div class="brand-lockup">
      <span class="mark-square"></span>
      <p class="brand-name"><span class="line-1">tidewell</span><span class="line-2">homecraft.</span></p>
      <div class="brand-rule"></div>
      <p class="brand-url">tidewellhomecraft.co.nz</p>
    </div>
  </section>
</body>
</html>
```